Park furniture company needs a new product flyer

We're a street and park furniture supply company and we have a new range of furniture that we would like to showcase to prospective customers.
Pictures, logo and copy attached.
Furniture pictures are also available with a black background.
Warranty information needs to feature on the flyer.
Recycled content information needs to feature on the flyer.

Target Market(s)

Landscape Architects

Font styles to use
Serif

Requirements
Must have
• Professional fonts and graphics.
Should not have
• comic sans or similar fonts - cheap graphics

```html
<!DOCTYPE html>
<html lang="en">
<head>
<meta charset="utf-8">
<title>Kestrel Parkline – Product Flyer</title>
<link rel="stylesheet" href="https://fonts.googleapis.com/css2?family=Montserrat:wght@400;600;800&family=Oswald:wght@500;600&display=swap">
<style>
  :root {
    --page-bg: #e6e6e6;
    --rust-top: #8e4426;
    --rust-mid: #6e2a17;
    --rust-deep: #58180d;
    --peach: #f1b489;
    --peach-bright: #f7c59d;
    --band-brown: #4a2a1c;
    --band-shadow: #2e120a;
    --tab-red: #8b1d12;
    --tab-edge: #a8321f;
    --ink: #2f3034;
  }
  * { box-sizing: border-box; margin: 0; padding: 0; }
  html, body {
    width: 1200px; height: 880px; overflow: hidden;
    background: var(--page-bg);
  }
  .flyer {
    position: absolute; left: 300px; top: 16px;
    width: 600px; height: 848px; overflow: hidden;
    background: linear-gradient(170deg, var(--rust-top) 0%, var(--rust-mid) 50%, var(--rust-deep) 100%);
    box-shadow: 0 6px 18px rgba(0,0,0,.25);
    font-family: "Montserrat", Arial, sans-serif;
  }
  .flyer__texture { position: absolute; inset: 0; }
  .brand {
    position: absolute; left: 38px; top: 66px;
    font-weight: 600; color: var(--ink);
    font-size: 54px; letter-spacing: 1px; line-height: 1;
    display: flex; align-items: center; gap: 12px;
  }
  .brand__mark { width: 14px; height: 14px; background: var(--ink); }
  .brand__sub { font-size: 20px; letter-spacing: 0; align-self: flex-end; margin-bottom: 4px; }
  .intro {
    position: absolute; left: 42px; top: 252px; width: 280px;
    color: var(--peach); font-size: 12px; line-height: 1.3;
    text-align: justify;
  }
  .intro p { margin-bottom: 11px; }
  .intro strong { font-weight: 800; color: var(--peach-bright); }
  .range-summary {
    position: absolute; left: 42px; top: 556px; width: 390px;
    font-family: "Oswald", "Arial Narrow", sans-serif; font-weight: 600;
    color: var(--peach); font-size: 20px; line-height: 1.2;
    text-transform: uppercase; letter-spacing: .5px;
    text-shadow: 1px 1px 0 var(--band-shadow);
  }
  .options-tab {
    position: absolute; right: 0; top: 672px; width: 200px; height: 72px;
    background: var(--tab-red);
    clip-path: polygon(18% 0, 100% 0, 100% 100%, 0 100%);
    border-top: 3px solid var(--tab-edge);
    padding: 10px 14px 0 56px;
    font-family: "Oswald", "Arial Narrow", sans-serif; font-weight: 600;
    color: var(--peach-bright); font-size: 15px; line-height: 1.15;
    text-transform: uppercase;
  }
  .length-band {
    position: absolute; left: 0; top: 744px; width: 470px; height: 70px;
    background: var(--band-brown);
    clip-path: polygon(0 0, 90% 0, 100% 100%, 0 100%);
    padding: 12px 0 0 42px;
    font-family: "Oswald", "Arial Narrow", sans-serif; font-weight: 500;
    color: var(--peach); font-size: 18px; line-height: 1.3;
  }
  .length-band__shadow {
    position: absolute; left: 80px; top: 814px; width: 420px; height: 8px;
    background: var(--band-shadow);
  }
</style>
</head>
<body>
  <article class="flyer">
    <svg class="flyer__texture" width="600" height="848" viewBox="0 0 600 848">
      <defs>
        <linearGradient id="timber" x1="0" y1="0" x2="1" y2="1">
          <stop offset="0" stop-color="#e4e2de"/>
          <stop offset=".5" stop-color="#c9c6c0"/>
          <stop offset="1" stop-color="#dcd9d4"/>
        </linearGradient>
      </defs>
      <path role="img" aria-label="Weathered grey timber texture behind the product range"
        fill="url(#timber)"
        d="M0 0 H600 V672 L580 680 L555 672 L530 678 L520 672 L505 640 L490 600 L470 550 L445 500 L420 440 L395 380 L372 300 L358 240 L345 214 L320 206 L300 200 L280 210 L255 200 L230 212 L205 206 L180 218 L150 210 L120 222 L95 212 L70 220 L45 208 L20 216 L0 210 Z"/>
      <rect role="img" aria-label="Product photographs of seats, benches and picnic tables" x="450" y="160" width="135" height="300" rx="4" fill="#b58a6a" opacity=".35"/>
    </svg>

    <div class="brand"><span class="brand__mark"></span><span>KESTREL</span><span class="brand__sub">Parkline</span></div>

    <div class="intro">
      <p>European inspired with a unique and original design, that is functional all while respecting the environment.</p>
      <p>Our range is designed to make life easier for people; created using extremely durable, ultra low maintenance materials.</p>
      <p>Featuring <strong>98% recycled</strong> composite battens in a range of stain and fade-resistant colour options and a unique aluminium frame design.</p>
      <p>The capped composite battens come with a 10-year commercial warranty covering staining, fading and structural performance.</p>
      <p>Site-specific for healthcare applications offering wheelchair accessibility options.</p>
    </div>

    <h2 class="range-summary">The Kestrel Parkline range comprises of a seat with optional armrests, bench seat and table, available in both standard or DDA designs</h2>

    <div class="options-tab">Bolt down or<br>freestanding<br>options.</div>

    <div class="length-band">Uniform length of 1800mm<br>with tailored options available.</div>
    <div class="length-band__shadow"></div>
  </article>
</body>
</html>
```